Walking Beside the Quiet River; A Study of Refuge, Purpose & Calling

I need a book cover, for the above book title. This is a journey of the heart to know the heart of God. I think on the text, Simple (see below graphic)
Black Lettering for Knowing.....Intimately
Gold lettering for God
Either gold or black for the subtitle; A Study of Refuge, Purpose, & Calling
I would like the below graphic idea only no photograph of a person,
and White background instead of black
Simple Font, like below graphic, but open to suggestions

Target Market(s)

not age specific, Every person has been given a heart to know God, we are taking the mystery out the process to understand God is Father, loving gracious, ever present, etc. If we know His heart, we realize He's not at a distance, He is there, an ever present help

Industry/Entity Type

Security

Requirements
Must have
• Title: Walking Beside the Quiet River; A Study of Refuge, Purpose, & Calling
• My name, Tom Pettigrew
Nice to have
• See Below Graphic

```html
<!DOCTYPE html>
<html lang="en">
<head>
<meta charset="utf-8">
<title>Walking Beside the Quiet River – Book Cover</title>
<link href="https://fonts.googleapis.com/css2?family=Bebas+Neue&family=Jost:wght@500;600&family=Roboto:ital,wght@0,400;0,500;1,400&display=swap" rel="stylesheet">
<style>
  :root {
    --ink: #0d0d0d;
    --gold: #d6b93e;
    --gold-text: #cdb13a;
    --paper: #ffffff;
    --paper-edge: #ecebe8;
    --body: #222222;
    --photo-warm: #7a4a2c;
    --photo-dark: #3a2618;
  }
  * { margin: 0; padding: 0; box-sizing: border-box; }
  html, body { width: 1200px; height: 877px; overflow: hidden; background: var(--paper); }
  .cover {
    position: relative; width: 1200px; height: 877px; overflow: hidden;
    background: radial-gradient(ellipse 75% 70% at 50% 35%, var(--paper) 0%, #f9f9f8 55%, var(--paper-edge) 100%);
    font-family: "Roboto", sans-serif; color: var(--body);
  }
  /* Back cover */
  .back { position: absolute; left: 47px; top: 78px; width: 499px; }
  .endorsement { margin-bottom: 19px; font-size: 13.6px; line-height: 19px; }
  .endorsement .quote { font-style: italic; text-align: justify; }
  .endorsement .who { font-weight: 500; color: var(--ink); }
  .endorsement .org { color: var(--gold-text); }
  .blurb { position: absolute; left: 47px; top: 400px; width: 499px; font-size: 13.8px; line-height: 18.2px; text-align: justify; }
  .author-photo {
    float: left; width: 134px; height: 189px; margin: 2px 12px 4px 0;
    background: linear-gradient(160deg, var(--photo-warm), var(--photo-dark));
  }
  .blurb p { margin-bottom: 14px; }
  .barcode-area { position: absolute; left: 362px; top: 727px; width: 190px; height: 114px; background: var(--paper); }
  /* Spine & front */
  .art { position: absolute; left: 0; top: 0; }
  .title-word { font-family: "Bebas Neue", sans-serif; fill: var(--ink); }
  .title-gold { font-family: "Bebas Neue", sans-serif; fill: var(--gold); }
  .subtitle { font-family: "Jost", sans-serif; font-weight: 600; font-size: 19px; letter-spacing: 4.2px; fill: var(--ink); }
  .author { font-family: "Jost", sans-serif; font-weight: 600; font-size: 38px; fill: var(--ink); }
  .spine-title { font-family: "Bebas Neue", sans-serif; font-size: 31px; fill: var(--ink); }
  .spine-author { font-family: "Jost", sans-serif; font-weight: 500; font-size: 25px; fill: var(--ink); }
</style>
</head>
<body>
<div class="cover">
  <section class="back">
    <div class="endorsement">
      <p class="quote">This book teaches Biblical truths that cross over generations, careers and callings because it is the “One thing” that matters always, knowing “Father God” intimately.</p>
      <p class="who">— Dana Pettigrew Hale</p>
      <p class="org">Harbor Award Nominated Christian Recording Artist</p>
    </div>
    <div class="endorsement">
      <p class="quote">We recommend Tom Pettigrew and this book as an expert resource, whether you’ve been on a quest for decades to know the love of God, or have just begun your adventure.</p>
      <p class="who">— Pastors Gerald &amp; Tessa Whitfield</p>
      <p class="org">Cedar Ridge Fellowship Church</p>
    </div>
    <div class="endorsement">
      <p class="quote">Tom Pettigrew is one of the best communicators of the heart of the Father I’ve ever heard. These truths will change your life forever!</p>
      <p class="who">— Martin &amp; Shelly Harlow</p>
      <p class="org">Deep Waters Global Ministries</p>
    </div>
  </section>

  <section class="blurb">
    <div class="author-photo" role="img" aria-label="Portrait photograph of the author and his wife"></div>
    <p>What if you didn’t have to do everything, be everything, and make everything happen? What if you could do away with guilt, ego, and self-doubt? What if instead of trying your hardest to be your best, you could simply trust God? What if you could just know God instead of having to know it all?</p>
    <p>It’s time to throw off man-made traditions and filters that complicate your life and have you trying to earn instead of simply receive God’s love. With humor, compassion, and clarity, <em>Walking Beside the Quiet River</em> reveals the heart of the Father in the person of Christ so you can put Him at the center of your Christianity, and get over yourself and into God.</p>
  </section>

  <div class="barcode-area"></div>

  <svg class="art" width="1200" height="877" viewBox="0 0 1200 877" xmlns="http://www.w3.org/2000/svg">
    <g class="spine">
      <text class="spine-title" transform="translate(589 60) rotate(90)" textLength="330" lengthAdjust="spacingAndGlyphs">WALKING BESIDE THE <tspan class="title-gold">QUIET</tspan> RIVER</text>
      <text class="spine-author" transform="translate(591 566) rotate(90)" textLength="242" lengthAdjust="spacing">TOM PETTIGREW</text>
    </g>
    <g class="front">
      <text class="title-word" x="660" y="203" font-size="176" textLength="486" lengthAdjust="spacingAndGlyphs">WALKING BESIDE THE</text>
      <text class="subtitle" x="904" y="269" text-anchor="middle">A STUDY OF REFUGE,</text>
      <text class="subtitle" x="904" y="300" text-anchor="middle">PURPOSE &amp; CALLING</text>
      <text class="title-gold" x="905" y="574" font-size="310" text-anchor="middle" textLength="420" lengthAdjust="spacingAndGlyphs">QUIET</text>
      <text class="author" x="904" y="674" text-anchor="middle" textLength="350" lengthAdjust="spacing">TOM PETTIGREW</text>
      <text class="title-word" x="662" y="808" font-size="106" textLength="482" lengthAdjust="spacing">RIVER</text>
    </g>
  </svg>
</div>
</body>
</html>
```